Text only wordpress site to capture emails

Refer to inspiration upload for list of sites that will be useful for you.

We need a site that will be used to capture emails from clients that follow us on social media. The site will be all text, pretty simple. I have a couple of text sites that I like and we can use them for an example.

Menu section will have home, archive, about.
Footer will have © and Website Privacy Policy | Legal and Policies
There will be some text on the home page and an email capture.

This site will be all text no pictures.

I discuss office politics so the text portions will have some questions and answers on this and then prompt for the visitor to subscribe to my email list.

The only purpose of the site is to build an email list from existing social media followers so the site will be pretty simple in and of itself.

• Text only, similar Q&A to uploaded pics.

I will use a template from mail lantern dotcom for email capture.

I like the simple couriernew font family that is on both sites supplied in the uploads.
• If you use any color it needs to be very minimal.

```html
<!DOCTYPE html>
<html lang="en">
<head>
<meta charset="utf-8">
<title>Tallow post</title>
<link rel="stylesheet" href="https://fonts.googleapis.com/css2?family=Courier+Prime:wght@400;700&display=swap">
<style>
  :root {
    --page: #ffffff;
    --ink: #111111;
    --body-ink: #333333;
    --muted: #999999;
    --field-border: #e6e6e6;
    --button: #222222;
    --button-ink: #f2f2f2;
  }
  * { box-sizing: border-box; margin: 0; padding: 0; }
  html, body {
    width: 1200px;
    height: 680px;
    overflow: hidden;
    background: var(--page);
    font-family: "Courier Prime", "Courier New", monospace;
    color: var(--ink);
  }
  .site {
    position: relative;
    width: 1200px;
    height: 680px;
  }
  .sidebar {
    position: absolute;
    left: 45px;
    top: 0;
    width: 210px;
    height: 680px;
  }
  .site-title {
    position: absolute;
    top: 44px;
    font-size: 25px;
    font-weight: 700;
    letter-spacing: 0.3px;
    white-space: nowrap;
  }
  .main-nav {
    position: absolute;
    top: 138px;
    list-style: none;
  }
  .main-nav li { height: 37px; font-size: 17.5px; }
  .main-nav a { color: var(--ink); text-decoration: none; }
  .main-nav .current { font-weight: 700; }
  .site-footer {
    position: absolute;
    top: 548px;
    font-size: 11px;
    color: var(--body-ink);
    line-height: 18.5px;
    letter-spacing: 0.3px;
  }
  .site-footer a { color: var(--body-ink); text-decoration: none; display: block; }
  .copyright { margin-top: 22px; }
  .content {
    position: absolute;
    left: 280px;
    top: 50px;
    width: 450px;
  }
  .intro {
    font-size: 15px;
    font-weight: 700;
    line-height: 24px;
    margin-bottom: 37px;
  }
  .faq dt {
    font-size: 11.5px;
    font-weight: 700;
    line-height: 21px;
  }
  .faq dd {
    font-size: 11.5px;
    line-height: 20.7px;
    color: var(--body-ink);
    margin-bottom: 20px;
    letter-spacing: 0.2px;
  }
  .signup {
    position: absolute;
    left: 794px;
    top: 54px;
    width: 350px;
  }
  .signup-heading {
    font-size: 17px;
    font-weight: 400;
    line-height: 21px;
    letter-spacing: 1.6px;
  }
  .signup-form {
    position: relative;
    margin-top: 46px;
    width: 335px;
    height: 32px;
  }
  .email-field {
    width: 250px;
    height: 32px;
    border: 1px solid var(--field-border);
    border-right: none;
    padding-left: 12px;
    font-family: inherit;
    font-size: 9.5px;
    color: var(--ink);
  }
  .email-field::placeholder { color: var(--muted); }
  .subscribe-button {
    position: absolute;
    right: 0;
    top: 0;
    width: 98px;
    height: 32px;
    border: none;
    border-radius: 16px;
    background: var(--button);
    color: var(--button-ink);
    font-family: inherit;
    font-size: 9.5px;
    letter-spacing: 0.5px;
  }
  .signup-note {
    margin-top: 24px;
    font-size: 13px;
    line-height: 17px;
    letter-spacing: 0.7px;
    color: var(--body-ink);
  }
</style>
</head>
<body>
<div class="site">
  <aside class="sidebar">
    <div class="site-title">Tallow post</div>
    <ul class="main-nav">
      <li><a class="current" href="#">Home</a></li>
      <li><a href="#">Archive</a></li>
      <li><a href="#">About</a></li>
    </ul>
    <footer class="site-footer">
      <a href="#">Website Privacy Policy</a>
      <a href="#">Legal and Policies</a>
      <p class="copyright">&copy;2021 Tallow post</p>
    </footer>
  </aside>

  <main class="content">
    <p class="intro">The tallow post is a market newsletter<br>for professional investors.</p>
    <dl class="faq">
      <dt>Q: why a newsletter?</dt>
      <dd>A: the stuff that's out there right now isn't very good. there are very few people that can write well in this business. did you know that i won several spelling bees growing up?</dd>
      <dt>Q: really!</dt>
      <dd>A: yup. but beyond that, there's stuff that's too literary, stuff that assumes you'll listen to every idea, and stuff that manages to get the direction right, but not the timing.</dd>
      <dt>Q: yours is better?</dt>
      <dd>A: mine is better. my goal is to make my commentary a joy to read, in addition to being super-smart and timely as hell.</dd>
      <dt>Q: how are you qualified?</dt>
      <dd>A: i was a trader for eight years; four of which as an ETF trader.</dd>
      <dt>Q: you weren't just a flow monkey?</dt>
      <dd>A: absolutely not.</dd>
      <dt>Q: how much are subscriptions?</dt>
      <dd>A: $795/year. a firm may purchase a site license. you can learn more here.</dd>
    </dl>
  </main>

  <section class="signup">
    <h2 class="signup-heading">The Latest Trends In Your<br>Inbox Every Week.</h2>
    <form class="signup-form">
      <input class="email-field" type="email" placeholder="Your Email">
      <button class="subscribe-button" type="button">Subscribe</button>
    </form>
    <p class="signup-note">Join the tallow post newsletter for all<br>updates in one place.</p>
  </section>
</div>
</body>
</html>
```